Packaging design for Virgin Coconut Oil. 100% pure cold pressed coconut oil

We need a new packaging and label design for our Virgin Coconut Oil product. It is currently marketed in the Philippines as a food supplement. We would like to try marketing it to other Asian countries such as Singapore, Malaysia and Hong Kong. The company has been producing this product since 2004 but now would like to venture into exporting our products overseas.

Would like to see designs with earth, natural "organic" colors. Fresh, Clean and pure look. Our trade mark is "Lunaria Grove". Its a 100% pure cold pressed virgin coconut oil. All in all, we want to totally repackage our product and re-design the trademark to cater to export markets. Thanks!

Mid to High

Health Product

cadf82
9bcb3b
33b8a4
ffffff
3176b5
3276b5
0592cd
fbed22
fece3e

• Bottle shape design ideas.

```html
<!DOCTYPE html>
<html lang="en">
<head>
<meta charset="utf-8">
<title>Lunaria Grove Virgin Coconut Oil Label</title>
<link href="https://fonts.googleapis.com/css2?family=Arvo:wght@700&family=Oswald:wght@500;600&display=swap" rel="stylesheet">
<style>
  :root {
    --page-bg: #ececec;
    --label-light: #e4f2c4;
    --label-mid: #cde6a0;
    --label-deep: #b5d97a;
    --leaf-green: #4e9a2c;
    --leaf-light: #8cc63f;
    --badge-cream: #f7f8e8;
    --badge-green: #2f8a4e;
    --brand-green: #2d8a4a;
    --band-brown: #6b4028;
    --band-brown-dark: #55311d;
    --accent-brown: #9a5a2e;
    --text-green: #2e8b3a;
    --text-dark: #1e1e1e;
    --coconut-green: #7fb23a;
    --white: #ffffff;
  }
  * { box-sizing: border-box; margin: 0; padding: 0; }
  html, body { width: 725px; height: 1200px; overflow: hidden; }
  body { background: var(--page-bg); font-family: "Oswald", sans-serif; }

  .label {
    position: absolute; left: 72px; top: 30px;
    width: 580px; height: 1140px; overflow: hidden;
    background: linear-gradient(180deg, var(--label-mid) 0%, var(--label-light) 45%, var(--label-mid) 100%);
  }
  .palm-leaves {
    position: absolute; left: 0; top: 0; width: 100%; height: 380px;
    background: radial-gradient(ellipse at 50% 0%, var(--leaf-green) 0%, var(--leaf-light) 45%, rgba(205,230,160,0) 75%);
  }
  .name-badge { position: absolute; left: 62px; top: 330px; width: 456px; height: 290px; }
  .name-badge svg { position: absolute; inset: 0; }
  .brand-name {
    position: absolute; left: 0; right: 0; top: 82px;
    text-align: center; font-family: "Arvo", serif; font-weight: 700;
    font-size: 68px; line-height: 1.05; color: var(--brand-green);
  }
  .coconuts {
    position: absolute; left: 170px; top: 625px; width: 250px; height: 205px;
    border-radius: 50% 50% 45% 45%;
    background: radial-gradient(ellipse at 50% 45%, var(--coconut-green) 0%, #a4c95a 55%, rgba(205,230,160,0) 75%);
  }
  .product-band {
    position: absolute; left: 0; right: 0; top: 836px; height: 62px;
    background: linear-gradient(180deg, var(--band-brown) 0%, var(--band-brown-dark) 100%);
    color: var(--white); text-align: center;
    font-size: 44px; font-weight: 600; line-height: 62px; letter-spacing: 0.5px;
  }
  .claims { position: absolute; left: 0; right: 0; top: 904px; text-align: center; }
  .claim { font-weight: 500; line-height: 1; }
  .claim-pure { color: var(--accent-brown); font-size: 27px; margin-top: 6px; }
  .claim-natural { color: var(--text-green); font-size: 27px; }
  .divider { width: 450px; margin: 11px auto; border-top: 2px dotted rgba(60,90,40,0.45); }
  .claim-since { color: var(--text-dark); font-size: 20px; margin-top: 22px; letter-spacing: 1px; }
  .claim-notice { color: var(--accent-brown); font-size: 21px; margin-top: 14px; }
  .volume {
    color: var(--text-dark); font-family: "Arvo", serif; font-weight: 700;
    font-size: 34px; margin-top: 24px;
  }
</style>
</head>
<body>
  <main class="label">
    <div class="palm-leaves" role="img" aria-label="Illustration of green palm fronds hanging from the top"></div>

    <div class="name-badge">
      <svg viewBox="0 0 456 290" width="456" height="290" aria-hidden="true">
        <path d="M40 40 L416 40 L416 62 Q436 62 436 82 L436 208 Q436 228 416 228 L416 250 L40 250 L40 228 Q20 228 20 208 L20 82 Q20 62 40 62 Z"
              fill="var(--badge-cream)" stroke="var(--badge-green)" stroke-width="4"/>
        <path d="M50 50 L406 50 L406 70 Q426 70 426 90 L426 200 Q426 220 406 220 L406 240 L50 240 L50 220 Q30 220 30 200 L30 90 Q30 70 50 70 Z"
              fill="none" stroke="var(--badge-green)" stroke-width="1.5"/>
      </svg>
      <div class="brand-name">Lunaria<br>Grove</div>
    </div>

    <div class="coconuts" role="img" aria-label="Illustration of two green coconuts with an opened coconut half"></div>

    <div class="product-band">VIRGIN COCONUT OIL</div>

    <div class="claims">
      <p class="claim claim-pure">100% PURE COLD PRESSED</p>
      <div class="divider"></div>
      <p class="claim claim-natural">ALL NATURAL FOOD SUPPLEMENT</p>
      <div class="divider"></div>
      <p class="claim claim-since">SINCE 2004</p>
      <p class="claim claim-notice">NO APPROVED THERAPEUTIC CLAIM</p>
      <p class="volume">1ℓ</p>
    </div>
  </main>
</body>
</html>
```